Design Tweak needed for a current site

Design on top of an existing quiz funnel

Ideally we would like to tweak what we have already built here (moving elements, styles, adding simple elements etc): http://offers.rateplumfinder.com/could-you-cut-your-auto-premium

The flow:
1) User lands on the quiz page
2) User answers X questions and moves through the flow
3) Calculating user results screen
4) User reaches a success screen, and is subsequently redirected

Keys to the design:
1) We need to emphasize the quiz title as that will drive engagement. In this case, this is a quiz to see if you might be eligible to save money on car insurance.

2) At the end of the quiz we need to make it very, very clear that the user is eligible for savings and that in order to complete the process they are being redirected to another page where they need to fill out a form. It is critical that the design communicates this very clearly... We can count down the time left until redirect and we can use any order of elements to make this point. I think our current design does a very bad job of this.

3) We want to have a "calculating" step so that it seems like the page is working in the background

Goals of the design:
1) Polished, high quality experience throughout
2) User is clearly prepared to be redirected to the conversion funnel/landing page at the end
3) User understands the value of completing the quiz

Target Market(s)

designers

Industry/Entity Type

Moving

Number of Pages Required

1 page

Font styles to use
Sans Serif

Colors

Designer to choose colors to be used in the design.

Requirements
Must have
• This quiz funnel is a template so while the current use case is for auto insurance, we would like a design that also would work in other contexts.
Should not have
• We don't want to materially change the core functionality of the quiz itself... redesigning any of the elements or interactions is encouraged though

```html
<!DOCTYPE html>
<html lang="en">
<head>
<meta charset="utf-8">
<title>QuoteLantern – Car Insurance Quiz</title>
<link rel="stylesheet" href="https://fonts.googleapis.com/css2?family=Libre+Franklin:wght@400;500;600;700&display=swap">
<style>
  :root {
    --sky-top: #d3e0dc;
    --sky-mid: #e6ebdc;
    --sky-low: #eef0de;
    --ground: #c9d1b5;
    --ink: #3f524c;
    --ink-soft: #4b5a55;
    --green: #6cc35f;
    --step-grey: #b9bdb9;
    --track: #d6d8d2;
    --card-bg: #e3e6d4;
    --card-edge: #cfd4bf;
    --white: #ffffff;
    --car-blue: #9fb7b2;
    --car-olive: #c5cca8;
    --car-green: #a9b38a;
    --string: #a9b39a;
    --brand-ink: #1d1d1d;
  }
  * { margin: 0; padding: 0; box-sizing: border-box; }
  html, body { width: 1200px; height: 771px; overflow: hidden; }
  body {
    position: relative;
    font-family: "Libre Franklin", Arial, sans-serif;
    color: var(--ink);
    background: linear-gradient(180deg, var(--sky-top) 0%, var(--sky-mid) 40%, var(--sky-low) 100%);
  }
  .ground { position: absolute; left: 0; right: 0; top: 743px; bottom: 0; background: var(--ground); }
  .string { position: absolute; top: 0; width: 1px; background: var(--string); }
  .car { position: absolute; border-radius: 22px 22px 10px 10px; opacity: .85; }

  .brand {
    position: absolute; top: 55px; left: 0; right: 0;
    display: flex; justify-content: center; align-items: center; gap: 9px;
    font-size: 26px; font-weight: 500; color: var(--brand-ink);
  }
  .brand-dot { width: 28px; height: 28px; border-radius: 50%; background: var(--brand-ink); }

  .quiz-title {
    position: absolute; top: 161px; left: 0; right: 0; text-align: center;
    font-size: 34px; font-weight: 700; letter-spacing: -.6px; color: var(--ink);
  }
  .quiz-sub {
    position: absolute; top: 213px; left: 0; right: 0; text-align: center;
    font-size: 20.5px; font-weight: 400; color: var(--ink-soft);
  }

  .steps-label { position: absolute; top: 297px; left: 298px; font-size: 19px; color: var(--ink-soft); }
  .track { position: absolute; top: 307px; left: 433px; width: 445px; height: 4px; background: var(--track); }
  .track-done { position: absolute; top: 306px; left: 440px; width: 47px; height: 6px; background: var(--green); }
  .step {
    position: absolute; top: 289px; width: 40px; height: 40px; border-radius: 50%;
    background: var(--white); border: 3px solid #dcdedb;
    box-shadow: 0 1px 3px rgba(0,0,0,.15);
    display: flex; align-items: center; justify-content: center;
    font-size: 20px; font-weight: 700; color: var(--step-grey);
  }
  .step.active { border-color: var(--green); }

  .question {
    position: absolute; top: 374px; left: 0; right: 0; text-align: center;
    font-size: 22px; font-weight: 500; color: var(--ink);
  }
  .option {
    position: absolute; top: 433px; width: 141px; height: 184px;
    background: var(--card-bg); border: 1px solid var(--card-edge); border-radius: 3px;
  }
  .option-icon {
    position: absolute; top: 8px; left: 8px; width: 125px; height: 125px;
    background: var(--white); border-radius: 3px;
    display: flex; align-items: center; justify-content: center;
  }
  .option-icon span { width: 66px; height: 70px; border-radius: 6px; background: #d9dcc8; }
  .option-label {
    position: absolute; top: 148px; left: 0; right: 0; text-align: center;
    font-size: 18px; color: var(--ink);
  }
</style>
</head>
<body>
  <div class="ground"></div>

  <div class="string" style="left:73px;height:96px"></div>
  <div class="car" role="img" aria-label="Hanging car illustration" style="left:43px;top:96px;width:60px;height:48px;background:var(--car-blue)"></div>
  <div class="string" style="left:1034px;height:115px"></div>
  <div class="car" role="img" aria-label="Hanging sedan illustration" style="left:958px;top:113px;width:135px;height:48px;background:var(--car-blue)"></div>
  <div class="string" style="left:1117px;height:262px"></div>
  <div class="car" role="img" aria-label="Hanging wagon illustration" style="left:1033px;top:260px;width:154px;height:59px;background:var(--car-olive)"></div>
  <div class="car" role="img" aria-label="Parked sedan illustration" style="left:197px;top:707px;width:161px;height:58px;background:var(--car-blue)"></div>
  <div class="car" role="img" aria-label="Small parked car illustration" style="left:790px;top:707px;width:100px;height:37px;background:var(--car-green)"></div>

  <header class="brand"><span class="brand-dot"></span>QuoteLantern</header>

  <h1 class="quiz-title">Quiz: Are You Overpaying For Car Insurance?</h1>
  <p class="quiz-sub">Take our five question quiz to see if you might be eligible for car insurance savings</p>

  <div class="steps-label">Questions:</div>
  <div class="track"></div>
  <div class="track-done"></div>
  <div class="step active" style="left:413px">1</div>
  <div class="step" style="left:524px">2</div>
  <div class="step" style="left:636px">3</div>
  <div class="step" style="left:747px">4</div>
  <div class="step" style="left:858px">5</div>

  <h2 class="question">Do You Lease Or Own:</h2>

  <div class="option" style="left:446px">
    <div class="option-icon" role="img" aria-label="Lease document icon"><span></span></div>
    <div class="option-label">I Lease!</div>
  </div>
  <div class="option" style="left:614px">
    <div class="option-icon" role="img" aria-label="Owned car with dollar icon"><span></span></div>
    <div class="option-label">I Own!</div>
  </div>
</body>
</html>
```